Pro-life non-profit needs a dynamic poster design for their Christmas Gala.

We need a poster design which plays off the name of the event, The Winter Lantern. The Winter Lantern, of course is the Baby Jesus. Our cause supports unborn children in Iowa. The gala will include a concert of popular Christmas music sung by top soloists backed by an orchestra. An original commissioned song, The Winter Lantern, will be premiered. Purple and gold colors immediately come to mind, but a designer should not feel constrained on colors. We need an editable design w/fonts. Photoshop w/layers or Illustrator files are good.

```html
<!DOCTYPE html>
<html lang="en">
<head>
<meta charset="utf-8">
<title>The Winter Lantern – A Pro-Life Christmas Gala</title>
<link href="https://fonts.googleapis.com/css2?family=Cinzel:wght@400;600;700&family=Lato:wght@300;400;700;900&display=swap" rel="stylesheet">
<style>
:root{
  --page:#d4d4d6;
  --purple-top:#3b0a5e;
  --purple-mid:#2a0747;
  --purple-bottom:#12001f;
  --gold:#c9a23a;
  --gold-light:#f1d77a;
  --gold-deep:#a8741a;
  --gold-text:#b48a2a;
  --white:#ffffff;
  --ink:#1b1022;
  --price:#a8700f;
}
*{margin:0;padding:0;box-sizing:border-box}
html,body{width:750px;height:1200px;overflow:hidden}
body{background:var(--page);font-family:"Lato",Arial,sans-serif;position:relative}

.poster{
  position:absolute;left:0;top:37px;width:750px;height:1126px;overflow:hidden;
  background:linear-gradient(180deg,var(--purple-top) 0%,var(--purple-mid) 45%,var(--purple-bottom) 100%);
  color:var(--white);
}

.ornaments{position:absolute;border-radius:45%;
  background:radial-gradient(circle at 45% 40%,rgba(255,255,255,.8) 0%,rgba(233,190,90,.65) 35%,rgba(160,110,30,.35) 60%,rgba(59,10,94,0) 75%);}
.ornaments--left{left:14px;top:0;width:140px;height:252px}
.ornaments--right{left:572px;top:0;width:162px;height:306px}

.frame-lines{position:absolute;left:0;top:0;width:750px;height:1126px;pointer-events:none}

.line{position:absolute;left:0;right:0;text-align:center;line-height:1;transform:translateY(-50%);white-space:nowrap}

.presenter{top:187px;font-size:16px;letter-spacing:5px;padding-left:5px;font-weight:400}
.occasion{top:223px;font-size:19px;letter-spacing:2px;padding-left:2px;font-weight:400}

.title{position:absolute;left:0;right:0;top:268px;height:125px;font-family:"Cinzel",Georgia,serif;font-weight:600;white-space:nowrap;line-height:1}
.title span.gold{
  background:linear-gradient(180deg,var(--gold-light) 0%,var(--gold) 50%,var(--gold-deep) 100%);
  -webkit-background-clip:text;background-clip:text;color:transparent}
.title__the{position:absolute;left:150px;top:0;font-size:40px;letter-spacing:1px}
.title__main{position:absolute;left:0;right:0;top:38px;text-align:center;font-size:56px}
.title__main .cap{font-size:86px}

.tagline{top:432px;font-size:22px;font-weight:300;letter-spacing:13px;padding-left:13px}

.date-rule{position:absolute;height:2px;background:var(--gold)}
.date-label{position:absolute;text-align:center;font-size:14px;letter-spacing:6px;line-height:1;transform:translateY(-50%)}
.date-month{top:517px;font-size:24px;color:var(--gold)}
.date-day{top:551px;font-size:50px;font-weight:900;letter-spacing:-1px}
.date-year{top:585px;font-size:23px;color:var(--gold)}

.venue{top:618px;font-size:17px;letter-spacing:5px;padding-left:5px}

.price{position:absolute;top:666px;height:52px;background:var(--white);border-radius:3px;
  display:flex;align-items:center;justify-content:center;text-align:center;color:var(--ink);line-height:1.1}
.price--amount{font-size:22px;font-weight:900;color:var(--price)}
.price--label{font-size:15px}

.includes{top:743px;font-size:17px;letter-spacing:4px;padding-left:4px;color:var(--gold-text)}
.speaker{top:812px;font-family:"Cinzel",Georgia,serif;font-weight:600;font-size:30px;color:#dcbd55}
.speaker .cap{font-size:40px}
.speaker-role{top:851px;font-size:15px;letter-spacing:13px;padding-left:13px}
.notice{top:915px;font-size:17px;letter-spacing:5px;padding-left:5px;color:var(--gold-text)}

.order-button{position:absolute;left:214px;top:951px;width:321px;height:27px;background:var(--white);border-radius:4px;
  color:var(--ink);font-size:17px;letter-spacing:5px;padding-left:5px;display:flex;align-items:center;justify-content:center}
.website{top:1009px;font-size:17px;letter-spacing:4px;padding-left:4px}
.website svg{vertical-align:-2px;margin-right:6px}
.phone{position:absolute;left:124px;top:1039px;transform:translateY(-50%);font-size:22px;font-weight:700;line-height:1;white-space:nowrap}
.phone svg{vertical-align:-3px;margin-right:4px}
.email{position:absolute;left:320px;top:1039px;transform:translateY(-50%);font-size:15px;line-height:1;white-space:nowrap}
.email svg{vertical-align:-2px;margin-right:4px}
</style>
</head>
<body>
<main class="poster">
  <div class="ornaments ornaments--left" role="img" aria-label="Cluster of hanging gold and white Christmas baubles"></div>
  <div class="ornaments ornaments--right" role="img" aria-label="Cluster of hanging gold and white Christmas baubles"></div>

  <svg class="frame-lines" viewBox="0 0 750 1126" aria-hidden="true">
    <g fill="none" stroke="#c9a23a" stroke-width="3">
      <polyline points="185,187 25,187 25,1090 725,1090 725,187 560,187"/>
    </g>
    <g fill="none" stroke="#c9a23a" stroke-width="2">
      <polyline points="200,966 111,966 111,1070 662,1070 662,966 547,966"/>
    </g>
  </svg>

  <p class="line presenter">HEARTLAND FOR LIFE PRESENTS</p>
  <p class="line occasion">THE TENTH ANNUAL FUNDRAISING BANQUET</p>

  <h1 class="title">
    <span class="title__the gold">THE</span>
    <span class="title__main"><span class="gold"><span class="cap">W</span>INTER <span class="cap">L</span>ANTERN</span></span>
  </h1>

  <p class="line tagline">A PRO-LIFE CHRISTMAS GALA</p>

  <span class="date-rule" style="left:158px;width:165px;top:529px"></span>
  <span class="date-rule" style="left:158px;width:165px;top:570px"></span>
  <span class="date-rule" style="left:428px;width:164px;top:529px"></span>
  <span class="date-rule" style="left:428px;width:164px;top:570px"></span>
  <p class="date-label" style="left:158px;width:172px;top:550px">SATURDAY</p>
  <p class="date-label" style="left:428px;width:172px;top:550px">5:30PM</p>
  <p class="line date-month">NOV</p>
  <p class="line date-day">21</p>
  <p class="line date-year">2020</p>

  <p class="line venue">ELM HOLLOW CENTER, MILLBROOK, IA</p>

  <div class="price price--amount" style="left:172px;width:71px">$60</div>
  <div class="price price--label" style="left:246px;width:113px">PERSON</div>
  <div class="price price--amount" style="left:391px;width:70px">$500</div>
  <div class="price price--label" style="left:464px;width:114px">TABLE FOR<br>TEN</div>

  <p class="line includes">COCKTAILS • DINNER • CHRISTMAS CONCERT</p>

  <p class="line speaker"><span class="cap">B</span>ISHOP <span class="cap">T</span>HOMAS <span class="cap">H</span>ALDANE</p>
  <p class="line speaker-role">SPECIAL GUEST SPEAKER</p>

  <p class="line notice">SEATING LIMITED • RESERVATIONS NEEDED</p>

  <p class="order-button">ORDER TICKETS ONLINE</p>

  <p class="line website"><svg width="13" height="13" viewBox="0 0 14 14" fill="none" stroke="#fff" stroke-width="1.2"><circle cx="7" cy="7" r="6"/><ellipse cx="7" cy="7" rx="2.6" ry="6"/><line x1="1" y1="7" x2="13" y2="7"/><line x1="2" y1="4" x2="12" y2="4"/><line x1="2" y1="10" x2="12" y2="10"/></svg>WWW.HEARTLANDFORLIFE.ORG</p>
  <p class="phone"><svg width="10" height="18" viewBox="0 0 10 18"><path d="M8 1 C3 3 1 6 1 9 C1 12 3 15 8 17 L9 14 C6 13 5 11 5 9 C5 7 6 5 9 4 Z" fill="#fff"/></svg>515-555-0147</p>
  <p class="email"><svg width="17" height="12" viewBox="0 0 17 12"><rect x="0.5" y="0.5" width="16" height="11" fill="#fff"/><path d="M1 1 L8.5 7 L16 1 M1 11 L6.5 5.5 M16 11 L10.5 5.5" stroke="#2a0747" stroke-width="1.2" fill="none"/></svg>EVENTS@HEARTLANDFORLIFE.ORG</p>
</main>
</body>
</html>
```